Web design for consulting advisory business company

We need a web for our business consulting company. The web should transmit simplicity, innovation, trust, and solid knowledge of what we do. Inspirational webs to take a look are: https://brindlemont.com/ and http://taviresul.com.br. Use blue colors.

Target Market(s)

Private companies

Industry/Entity Type

Management Consulting

Number of Pages Required

5+ page

Font styles to use
Serif
Sans Serif

Colors
3176b5
3276b5
85abd2
85cae6
33a6d7
0592cd
ffffff
1b1b1b
474747

Requirements
Must have
• - use of blue
• - images
• - same version in different languages (portugueses and spanish)
Nice to have
• - white as background

```html
<!DOCTYPE html>
<html lang="en">
<head>
<meta charset="utf-8">
<title>Halvard Partners — Management Consulting</title>
<link rel="stylesheet" href="https://fonts.googleapis.com/css2?family=Montserrat:wght@400;500;600;700&family=Open+Sans:wght@400;600&display=swap">
<style>
:root{
  --blue:#3a6fe2;
  --blue-dark:#2a58c4;
  --blue-soft:#85abd2;
  --sky:#eaf1fb;
  --sky-2:#dbe7f8;
  --ink:#1b1b1b;
  --text:#474747;
  --muted:#8a93a3;
  --line:#e3e8ef;
  --white:#ffffff;
}
*{box-sizing:border-box;margin:0;padding:0}
html,body{width:1200px;height:2464px;overflow:hidden;background:var(--white)}
body{font-family:"Open Sans",Arial,sans-serif;color:var(--text);font-size:13px;line-height:1.55}
h1,h2,h3,h4,.brand,.nav{font-family:"Montserrat",Arial,sans-serif;color:var(--ink)}
a{color:inherit;text-decoration:none}
.wrap{width:1080px;margin:0 auto;position:relative}

/* top bar + header */
.topbar{height:28px;font-size:11px;color:var(--muted);border-bottom:1px solid var(--line)}
.topbar .wrap{display:flex;align-items:center;height:28px;gap:24px}
.topbar .help{color:var(--blue);font-weight:600;margin-right:auto}
.dots{display:flex;gap:6px}
.dots i{width:10px;height:10px;border-radius:50%;background:var(--blue-soft);display:block}
.header{height:72px}
.header .wrap{display:flex;align-items:center;height:72px}
.brand{display:flex;align-items:center;gap:10px;font-weight:700;font-size:22px;color:var(--blue);letter-spacing:1px;margin-right:auto}
.brand .mark{width:26px;height:26px;background:var(--blue)}
.nav{display:flex;gap:28px;font-size:13px;font-weight:500;align-items:center}
.nav .active{background:var(--blue);color:var(--white);padding:7px 16px;border-radius:16px}
.tools{display:flex;gap:18px;margin-left:40px;align-items:center}
.menu-box{width:34px;height:34px;border:1px solid var(--line);display:flex;align-items:center;justify-content:center}

/* hero */
.hero{height:384px;background:linear-gradient(90deg,#f2f4f7 0%,#e6eaf0 60%,#d9dee6 100%);position:relative;overflow:hidden}
.hero-photo{position:absolute;right:60px;top:0;width:560px;height:384px;background:radial-gradient(ellipse at 55% 45%,#c9ced6 0%,#dde1e7 55%,rgba(230,234,240,0) 80%)}
.hero .wrap{padding-top:66px}
.hero h1{font-size:54px;line-height:1.12;font-weight:600;color:var(--blue);width:500px}
.hero p{width:430px;margin-top:26px;font-size:14px}
.btns{display:flex;gap:18px;margin-top:30px;align-items:center}
.btn{display:inline-flex;align-items:center;gap:10px;background:var(--blue);color:var(--white);font-family:"Montserrat",sans-serif;font-weight:600;font-size:12px;padding:10px 22px;border-radius:20px}
.play{width:20px;height:20px;border-radius:50%;background:var(--white);display:flex;align-items:center;justify-content:center}

/* intro + features */
.intro{text-align:center;padding-top:100px}
.intro h2{font-size:27px;font-weight:400;line-height:1.4;color:var(--text)}
.features{display:flex;justify-content:space-between;width:900px;margin:60px auto 0}
.feature{width:260px;text-align:center}
.feature-art{width:200px;height:80px;margin:0 auto;display:flex;align-items:center;justify-content:center;background:radial-gradient(ellipse at 50% 55%,#e3ecfb 0%,#eef3fc 50%,rgba(255,255,255,0) 72%)}
.feature h3{font-size:24px;font-weight:500;color:var(--blue);margin-top:6px}
.feature p{font-size:11px;margin-top:6px;color:var(--muted)}
.feature a{font-size:11px;color:var(--blue);text-decoration:underline;display:inline-block;margin-top:8px}

/* industries */
.industries{position:absolute;top:948px;left:0;width:1200px;height:740px;background:linear-gradient(180deg,var(--sky) 0%,var(--sky-2) 100%)}
.industries h2{text-align:center;font-size:40px;font-weight:500;padding-top:92px}
.ind-card{width:980px;margin:40px auto 0;background:var(--white);border-radius:4px;box-shadow:0 6px 24px rgba(40,70,130,.08);overflow:hidden}
.ind-grid{display:grid;grid-template-columns:repeat(3,1fr);gap:34px 40px;padding:42px 50px 36px}
.ind{display:flex;gap:14px}
.ind svg{flex:none}
.ind h4{font-size:16px;font-weight:500}
.ind p{font-size:11px;color:var(--muted);line-height:1.45;margin-top:4px}
.ind-bar{background:var(--blue);color:var(--white);display:flex;align-items:center;justify-content:space-between;padding:14px 50px;font-size:14px}
.ind-bar .quote{background:var(--white);color:var(--ink);font-size:11px;font-weight:600;padding:7px 16px;border-radius:16px;font-family:"Montserrat",sans-serif}

/* contact strip */
.reach{position:absolute;top:1688px;left:0;width:1200px;height:330px;background:linear-gradient(180deg,#3f75e6,#2f62d6);color:var(--white);overflow:hidden}
.reach-map{position:absolute;inset:30px 80px;background:radial-gradient(ellipse at 30% 50%,rgba(255,255,255,.08),transparent 60%),radial-gradient(ellipse at 70% 50%,rgba(255,255,255,.07),transparent 55%)}
.reach-cols{position:relative;display:flex;justify-content:space-between;width:960px;margin:0 auto;padding-top:70px}
.reach-col{width:260px;text-align:center}
.reach-col h3{color:var(--white);font-size:26px;font-weight:400;margin-top:12px}
.reach-col p{font-size:11px;opacity:.85;margin-top:8px}
.reach-col a{font-size:11px;text-decoration:underline;display:inline-block;margin-top:8px}

/* newsletter */
.news{position:absolute;top:2018px;left:0;width:1200px;height:58px;border-bottom:1px solid var(--line)}
.news .wrap{display:flex;align-items:center;height:58px;gap:14px;font-size:12px}
.news-field{margin-left:auto;width:300px;height:30px;border:1px solid var(--line);border-radius:15px;font-size:11px;color:var(--muted);padding:6px 14px}
.news .btn{padding:7px 18px;font-size:11px}

/* footer */
.footer{position:absolute;top:2076px;left:0;width:1200px;height:340px}
.footer .wrap{display:grid;grid-template-columns:250px 260px 260px 250px;gap:20px;padding-top:36px}
.footer h4{font-size:17px;font-weight:500;margin-bottom:14px}
.footer p,.footer li{font-size:11px;color:var(--text)}
.footer ul{list-style:none}
.links{display:flex;gap:50px;margin-top:14px}
.links li{line-height:2.1}
.article{margin-bottom:12px}
.article b{display:block;font-size:12px;font-weight:600;color:var(--ink)}
.article span{font-size:10px;color:var(--muted)}
.field{height:30px;border:1px solid var(--line);border-radius:15px;font-size:11px;color:var(--muted);padding:6px 14px;margin-bottom:10px}
.outline{display:inline-block;border:1px solid var(--blue);color:var(--blue);border-radius:15px;font-size:11px;padding:5px 16px;margin-top:14px}
.social{display:flex;gap:10px;margin-top:16px}
.social i{width:14px;height:14px;border-radius:50%;background:var(--blue-soft);display:block}
.copy{position:absolute;top:2416px;left:0;width:1200px;height:48px;border-top:1px solid var(--line);font-size:11px;color:var(--muted)}
.copy .wrap{line-height:48px}
</style>
</head>
<body>

<div class="topbar"><div class="wrap">
  <span class="help">Need Help? Ask Financial Advisor</span>
  <span>+1 (555) 014-2290</span>
  <span>hello@halvardpartners.com</span>
  <span>Contact</span>
  <span class="dots"><i></i><i></i><i></i></span>
</div></div>

<header class="header"><div class="wrap">
  <div class="brand"><span class="mark"></span>HALVARD PARTNERS</div>
  <nav class="nav">
    <a class="active">Home</a><a>About</a><a>Services</a><a>Case Studies</a><a>Insights</a><a>Contacts</a>
  </nav>
  <div class="tools">
    <svg width="16" height="16" viewBox="0 0 16 16" fill="none" stroke="#1b1b1b" stroke-width="2"><circle cx="7" cy="7" r="5"/><path d="M11 11l4 4"/></svg>
    <span class="menu-box"><svg width="14" height="12" viewBox="0 0 14 12" stroke="#1b1b1b" stroke-width="2"><path d="M0 1h14M0 6h14M0 11h14"/></svg></span>
  </div>
</div></header>

<section class="hero">
  <div class="hero-photo" role="img" aria-label="Portrait of a smiling senior consultant in a white shirt"></div>
  <div class="wrap">
    <h1>The fastest way to achieve success</h1>
    <p>To succeed in business today, you need to be flexible and have good planning and organizational skills.</p>
    <div class="btns">
      <a class="btn">Our Services</a>
      <a class="btn"><span class="play"><svg width="8" height="8" viewBox="0 0 8 8"><path d="M1 0l7 4-7 4z" fill="#3a6fe2"/></svg></span>Watch the Presentation</a>
    </div>
  </div>
</section>

<section class="intro">
  <h2>We bring the right people together to challenge established<br>thinking and drive transformation.</h2>
  <div class="features">
    <div class="feature">
      <div class="feature-art" role="img" aria-label="Soft blue cloud illustration with a document icon">
        <svg width="30" height="26" viewBox="0 0 30 26" fill="none" stroke="#3a6fe2" stroke-width="2.5"><rect x="2" y="2" width="26" height="22" rx="3"/><path d="M8 11h14M8 17h9"/></svg>
      </div>
      <h3>We Innovate</h3>
      <p>We find new ways to help our clients grow and change with the market.</p>
      <a>Read more</a>
    </div>
    <div class="feature">
      <div class="feature-art" role="img" aria-label="Soft blue cloud illustration with a rising chart icon">
        <svg width="36" height="26" viewBox="0 0 36 26" fill="none" stroke="#3a6fe2" stroke-width="2.5"><path d="M3 19l10-12 8 6 13-12"/><path d="M1 24h34"/></svg>
      </div>
      <h3>Performance</h3>
      <p>Performance is about helping each client achieve lasting results.</p>
      <a>Read more</a>
    </div>
    <div class="feature">
      <div class="feature-art" role="img" aria-label="Soft blue cloud illustration with an open envelope icon">
        <svg width="34" height="26" viewBox="0 0 34 26" fill="none" stroke="#3a6fe2" stroke-width="2.5"><path d="M2 11L17 2l15 9v13H2z"/><path d="M2 11l15 8 15-8"/></svg>
      </div>
      <h3>A Full Service</h3>
      <p>We cover all your business needs, from strategy to execution.</p>
      <a>Read more</a>
    </div>
  </div>
</section>

<section class="industries">
  <h2>Industries</h2>
  <div class="ind-card">
    <div class="ind-grid">
      <div class="ind"><svg width="30" height="30" viewBox="0 0 30 30" fill="none" stroke="#3a6fe2" stroke-width="2"><circle cx="15" cy="15" r="11"/><circle cx="15" cy="15" r="5"/></svg><div><h4>Strategy &amp; Planning</h4><p>A business strategy is the means by which it sets out to achieve its desired ends.</p></div></div>
      <div class="ind"><svg width="30" height="30" viewBox="0 0 30 30" fill="none" stroke="#3a6fe2" stroke-width="2"><rect x="4" y="8" width="22" height="16" rx="2"/><path d="M4 13h22"/></svg><div><h4>Finance &amp; Restructuring</h4><p>We help companies reorganize debt and operations to restore stability.</p></div></div>
      <div class="ind"><svg width="30" height="30" viewBox="0 0 30 30" fill="none" stroke="#3a6fe2" stroke-width="2"><path d="M4 14l11-9 11 9v12H4z"/></svg><div><h4>Estate Planning</h4><p>We plan the transfer of assets so families keep more of what they built.</p></div></div>
      <div class="ind"><svg width="30" height="30" viewBox="0 0 30 30" fill="none" stroke="#3a6fe2" stroke-width="2"><rect x="6" y="4" width="18" height="22" rx="2"/><path d="M10 11h10M10 16h10M10 21h6"/></svg><div><h4>Audit &amp; Evaluation</h4><p>If you have been selected for an audit, we will guide you through it.</p></div></div>
      <div class="ind"><svg width="30" height="30" viewBox="0 0 30 30" fill="none" stroke="#3a6fe2" stroke-width="2"><circle cx="15" cy="15" r="11"/><path d="M15 8v14M11 12h7M11 18h7"/></svg><div><h4>Taxes &amp; Efficiency</h4><p>We find ways to lower tax costs and improve your overall efficiency.</p></div></div>
      <div class="ind"><svg width="30" height="30" viewBox="0 0 30 30" fill="none" stroke="#3a6fe2" stroke-width="2"><path d="M5 8h3l3 13h12l3-9H10"/><circle cx="12" cy="25" r="1.5"/><circle cx="22" cy="25" r="1.5"/></svg><div><h4>Consumer Markets</h4><p>We help brands understand buyers and grow in changing markets.</p></div></div>
      <div class="ind"><svg width="30" height="30" viewBox="0 0 30 30" fill="none" stroke="#3a6fe2" stroke-width="2"><path d="M15 4l10 4v7c0 6-4 10-10 12-6-2-10-6-10-12V8z"/></svg><div><h4>Insurance</h4><p>We help insurers manage risk and build products clients can trust.</p></div></div>
      <div class="ind"><svg width="30" height="30" viewBox="0 0 30 30" fill="none" stroke="#3a6fe2" stroke-width="2"><path d="M5 7h20v13H12l-5 4v-4H5z"/></svg><div><h4>Communications</h4><p>We guide telecom and media firms through fast digital change.</p></div></div>
      <div class="ind"><svg width="30" height="30" viewBox="0 0 30 30" fill="none" stroke="#3a6fe2" stroke-width="2"><path d="M4 26h22M7 22V13M13 22V13M17 22V13M23 22V13M4 11l11-7 11 7z"/></svg><div><h4>Financial Services</h4><p>We support banks and funds in strategy, risk and operations.</p></div></div>
    </div>
    <div class="ind-bar">
      <span>Are you looking for professional advice for your business or your industry?</span>
      <a class="quote">Get a Free Quote</a>
    </div>
  </div>
</section>

<section class="reach">
  <div class="reach-map" role="img" aria-label="Faint world map in the background"></div>
  <div class="reach-cols">
    <div class="reach-col">
      <svg width="40" height="40" viewBox="0 0 40 40" fill="none" stroke="#fff" stroke-width="2"><path d="M20 36s-11-11-11-19a11 11 0 0122 0c0 8-11 19-11 19z"/><circle cx="20" cy="17" r="4"/></svg>
      <h3>Our Offices</h3>
      <p>Visit one of our offices to meet our advisors and talk about your plans.</p>
      <a>Locate the nearest office</a>
    </div>
    <div class="reach-col">
      <svg width="40" height="40" viewBox="0 0 40 40" fill="none" stroke="#fff" stroke-width="2"><rect x="5" y="10" width="30" height="20" rx="2"/><path d="M5 11l15 11 15-11"/></svg>
      <h3>Drop a Line</h3>
      <p>Send us a message and we will answer within one business day.</p>
      <a>Write now</a>
    </div>
    <div class="reach-col">
      <svg width="40" height="40" viewBox="0 0 40 40" fill="none" stroke="#fff" stroke-width="2"><circle cx="20" cy="14" r="6"/><path d="M8 34c0-7 5-12 12-12s12 5 12 12"/></svg>
      <h3>Careers</h3>
      <p>Join our growing team and build your career with bright colleagues.</p>
      <a>See open positions</a>
    </div>
  </div>
</section>

<section class="news"><div class="wrap">
  <svg width="22" height="16" viewBox="0 0 22 16" fill="none" stroke="#3a6fe2" stroke-width="2"><rect x="1" y="1" width="20" height="14" rx="2"/><path d="M1 2l10 7 10-7"/></svg>
  <span>Keep up to date — get updates with latest topics.</span>
  <span class="news-field">Your email address</span>
  <a class="btn">Sign me up</a>
</div></section>

<footer class="footer"><div class="wrap">
  <div>
    <div class="brand" style="font-size:18px"><span class="mark" style="width:22px;height:22px"></span>HALVARD PARTNERS</div>
    <p style="margin-top:16px">When you need advice on your next step, our team brings the clarity and experience to help you grow with confidence.</p>
    <a class="outline">Read More</a>
  </div>
  <div>
    <h4>Work Time</h4>
    <p>Mon – Fri: 9:00 – 18:00<br>Closed on Weekends</p>
    <div class="links">
      <ul><li>About</li><li>Aproach</li><li>People</li><li>Reviews</li><li>Insights</li></ul>
      <ul><li>Services</li><li>Industries</li><li>Case Studies</li><li>Shop</li><li>Contacts</li></ul>
    </div>
  </div>
  <div>
    <h4>Articles</h4>
    <div class="article"><b>US Stocks Are Expensive</b><span>Jan 12, 2024</span></div>
    <div class="article"><b>Investment Update: Fourth Quarter 2023</b><span>Dec 28, 2023</span></div>
    <div class="article"><b>Four Big Mistakes Your Small Business Is Making</b><span>Dec 04, 2023</span></div>
  </div>
  <div>
    <h4>Request a Call Back</h4>
    <div class="field">Name</div>
    <div class="field">Phone</div>
    <div class="field">Finance &amp; Restructuring ▾</div>
    <a class="btn" style="padding:7px 22px;font-size:11px">Send</a>
    <div class="social"><i></i><i></i><i></i><i></i></div>
  </div>
</div></footer>

<div class="copy"><div class="wrap">© 2024 Halvard Partners</div></div>

</body>
</html>
```